Web portal for events

The project is about creating a web application - portal for culture events in Denmark.

Design

We aim for very simplistic, light and fully responsive design. The white background is preferable, as well as light color tones. As inspirational points we like the colors used in www.brimvale.com and www.tallowpine.org

FORMAT AND REQUIREMENTS:
1. Design should be provided based on the wireframes specified as a link below.
2. The design (and all of its pages) should be provided in three resolution variants:
- Desktop
- Tablet
- Phone
3. The design should be provided as PSD, where each page/section should be in its own PSD file
4. All graphical elements in the design should be delivered as single layers which can then be extracted from the PSD.
5. All graphical elements (icons, graphical buttons, etc.) should be provided as vector objects in the PSD, so that they can be exported into different sizes without loss of quality (for responsiveness)
6. The design should use either web safe fonts or Google Fonts.

RESPONSIVENESS
The web application should be visible on any devices (i.e. responsive design)

WIREFRAMES:
https://quillmarsh.examplewire.com/projects/eventloom/prototype/Homepage?key=0000000000000000000000000000000000000000

We expect design of the following wireframes:

Homepage:
https://quillmarsh.examplewire.com/projects/eventloom/Homepage

For arrangører - billede uploaded:
https://quillmarsh.examplewire.com/projects/eventloom/For%20arrang%C3%B8rer%20-%20billede%20uploaded

Further specifications of the project (i.e. functionality, etc.):
https://files.dorvexa.com/document/d/0AbCdEfGhIjKlMnOpQrStUvWxYz0123456789abcdefg/edit?usp=sharing
Updates

```html
<!DOCTYPE html>
<html lang="da">
<head>
<meta charset="utf-8">
<title>KULTRA – Din Guide til kultur og events</title>
<link href="https://fonts.googleapis.com/css2?family=Open+Sans:wght@300;400;600&display=swap" rel="stylesheet">
<style>
:root{
  --orange:#f1735a;
  --orange-dark:#e25f46;
  --dark:#3b3b3b;
  --footer:#363636;
  --yellow:#f8c33d;
  --text:#777;
  --muted:#a4a4a4;
  --line:#e6e6e6;
  --white:#fff;
}
*{margin:0;padding:0;box-sizing:border-box}
html,body{width:767px;height:1200px;overflow:hidden;background:var(--white);font-family:"Open Sans",Arial,sans-serif;color:var(--text)}
.page{position:relative;width:767px;height:1200px}
.abs{position:absolute}

/* header */
.site-header{left:0;top:0;width:767px;height:78px;background:var(--orange)}
.brand{left:110px;top:8px;color:var(--white)}
.brand-name{font-size:34px;font-weight:600;letter-spacing:.5px;line-height:40px}
.brand-tag{font-size:7px;margin-top:3px}
.auth{top:14px;right:109px;display:flex;gap:22px;font-size:7.5px;color:var(--white);letter-spacing:.3px}
.search{left:384px;top:38px;width:274px;height:25px;background:var(--white);border-radius:2px;font-size:7.5px;color:#aaa;padding:8px 12px}
.search svg{position:absolute;right:9px;top:6px}

/* hero */
.hero-img{left:110px;top:93px;width:378px;height:213px;background:linear-gradient(120deg,#6f8f55 0%,#b9c3b0 45%,#e3d2a0 65%,#9ab6d0 100%)}
.hero-stripe{left:488px;top:93px;width:5px;height:213px;background:var(--orange)}
.hero-panel{left:493px;top:93px;width:165px;height:213px;background:var(--dark);color:var(--white);padding:22px 20px 0 20px}
.hero-panel::before{content:"";position:absolute;left:0;top:25px;border-left:6px solid var(--orange);border-top:6px solid transparent;border-bottom:6px solid transparent}
.hero-title{font-size:10.5px;line-height:13.5px;font-weight:400}
.hero-text{font-size:6.8px;line-height:12.6px;color:#c8c8c8;margin-top:9px;text-align:justify}
.hero-meta{position:absolute;left:20px;right:20px;top:143px;display:flex;justify-content:space-between;align-items:center;font-size:6.8px;color:#c8c8c8}
.hero-date{display:flex;align-items:center;gap:5px}
.hero-nav{position:absolute;right:0;bottom:0;display:flex;gap:2px}
.hero-nav span,.fav-nav span{display:flex;align-items:center;justify-content:center;width:17px;height:16px;background:#2e2e2e}

/* tabs */
.tabs{left:110px;top:318px;width:363px;height:30px;border-bottom:1px solid var(--line);display:flex;font-size:9.4px;color:#888}
.tab{padding:0 6.3px;line-height:30px}
.tab.active{background:var(--dark);color:var(--white);padding:0 8px;position:relative}
.tab.active::after{content:"";position:absolute;left:50%;bottom:-5px;margin-left:-4px;border-top:5px solid var(--dark);border-left:4px solid transparent;border-right:4px solid transparent}

/* listing head */
.list-title{left:109px;top:366px;font-size:13.6px;color:#555}
.sort{left:242px;top:369px;display:flex;align-items:center;gap:4px;font-size:9px;color:#777}
.sort-label{margin-right:5px}
.sort-box{height:16px;border:1px solid var(--line);font-size:6.5px;color:#999;display:flex;align-items:center;justify-content:center;gap:10px}

/* events grid */
.events{left:110px;top:406px;width:364px;display:grid;grid-template-columns:repeat(3,112px);column-gap:14px;grid-auto-rows:170px}
.event-img{width:112px;height:85px}
.event-title{font-size:9.6px;color:#8a8a8a;margin-top:8px}
.event-desc{font-size:6.5px;line-height:12px;color:#aaa;margin-top:2px}
.event-links{display:flex;justify-content:space-between;font-size:8.8px;margin-top:3px;color:#8a8a8a}
.event-links .see{color:var(--orange)}

/* pagination */
.pager{left:145px;top:1096px;width:290px;height:20px;display:flex;align-items:center;font-size:8px;color:#555}
.pager .prev,.pager .next{font-weight:600;display:flex;align-items:center;gap:5px}
.pager .sep{width:1px;height:24px;background:var(--line)}
.pager .nums{display:flex;gap:0;margin:0 20px 0 20px}
.pager .nums span{width:22px;text-align:center}

/* favorites */
.fav-head{left:493px;top:319px;width:165px;height:29px;background:var(--orange);color:var(--white);font-size:13.6px;line-height:29px;padding-left:12px}
.fav-nav{position:absolute;right:6px;top:7px;display:flex;gap:2px}
.fav-nav span{background:transparent;width:14px;height:14px}
.fav-list{left:493px;top:362px;width:165px}
.fav-item{display:flex;gap:9px;height:88px;border-bottom:1px solid #f0f0f0;margin-bottom:0;padding-top:0}
.fav-thumb{width:64px;height:64px;flex:none}
.fav-title{font-size:8.8px;color:#777}
.fav-text{font-size:6.3px;line-height:12px;color:#aaa;margin-top:5px;text-align:justify}
.fav-btn{left:525px;top:706px;width:101px;height:23px;background:var(--orange);color:var(--white);font-size:9.4px;text-align:center;line-height:23px;border-radius:2px}

/* newsletter */
.news-head{left:493px;top:742px;width:165px;height:28px;background:var(--dark);color:var(--white);font-size:12.8px;line-height:28px;padding-left:13px}
.news-body{left:493px;top:770px;width:165px;height:104px;background:var(--yellow);padding:8px 11px}
.news-text{font-size:7px;line-height:12px;color:var(--white);text-align:justify}
.news-form{position:absolute;left:11px;top:66px;display:flex;gap:5px}
.news-input{width:109px;height:25px;background:var(--white);font-size:6px;color:#999;padding:9px 8px}
.news-btn{width:32px;height:25px;background:var(--white);display:flex;align-items:center;justify-content:center}

/* promo */
.promo-img{left:493px;top:886px;width:165px;height:116px;background:linear-gradient(160deg,#2a2d4a 0%,#7a4a6a 45%,#d8533f 75%,#f2b24a 100%)}
.promo-corner{left:618px;top:886px;width:40px;height:40px;background:var(--orange);clip-path:polygon(0 0,100% 0,100% 100%)}
.promo-plus{left:640px;top:890px}
.promo-body{left:493px;top:1002px;width:165px;height:72px;background:var(--dark);padding:7px 16px}
.promo-title{font-size:9.8px;color:var(--white)}
.promo-text{font-size:6.4px;line-height:13px;color:#bbb;margin-top:3px}

/* footer */
.site-footer{left:0;top:1139px;width:767px;height:61px;background:var(--footer);color:#aaa;font-size:7px}
.copy{position:absolute;left:110px;top:15px}
.foot-links{position:absolute;left:110px;top:37px;display:flex;gap:4px;font-size:6.8px}
.foot-links .bar{color:#777}
.social{position:absolute;left:601px;top:30px;display:flex;gap:8px}
.social span{width:8px;height:8px;border-radius:50%;background:#5a5a5a}
</style>
</head>
<body>
<div class="page">

  <header class="site-header abs">
    <div class="brand abs">
      <div class="brand-name">KULTRA</div>
      <div class="brand-tag">Din Guide til kultur og events</div>
    </div>
    <nav class="auth abs"><span>LOGIN</span><span>SIGN UP</span></nav>
    <div class="search abs">Avanceret Søgning
      <svg width="12" height="12" viewBox="0 0 12 12"><circle cx="5" cy="5" r="3.8" fill="none" stroke="#bbb" stroke-width="1.3"/><line x1="7.8" y1="7.8" x2="11" y2="11" stroke="#bbb" stroke-width="1.5"/></svg>
    </div>
  </header>

  <div class="hero-img abs" role="img" aria-label="Two young people riding bicycles in a park"></div>
  <div class="hero-stripe abs"></div>
  <section class="hero-panel abs">
    <h2 class="hero-title">Lorem ipsum dolor sit amet, consectetur</h2>
    <p class="hero-text">Quisque accumsan eleifend dolor, nec bibendum nibh ultricies at. Nunc convallis risus sit amet augue bibendum non lobortis eros interdum. Maecenas quis risus felis, at volutpat elit...</p>
    <div class="hero-meta">
      <svg width="10" height="10" viewBox="0 0 10 10"><path d="M5 0v10M0 5h10" stroke="#fff" stroke-width="1.6"/></svg>
      <span class="hero-date"><svg width="9" height="9" viewBox="0 0 10 10"><circle cx="5" cy="5" r="4.2" fill="none" stroke="#c8c8c8"/><path d="M5 2.5V5h2" fill="none" stroke="#c8c8c8"/></svg>14th April 2013</span>
    </div>
    <div class="hero-nav">
      <span><svg width="5" height="7" viewBox="0 0 5 7"><path d="M4 0.5L1 3.5 4 6.5" fill="none" stroke="#fff" stroke-width="1.3"/></svg></span>
      <span><svg width="5" height="7" viewBox="0 0 5 7"><path d="M1 0.5L4 3.5 1 6.5" fill="none" stroke="#fff" stroke-width="1.3"/></svg></span>
    </div>
  </section>

  <nav class="tabs abs">
    <span class="tab active">Alle</span><span class="tab">Musik</span><span class="tab">Sport</span><span class="tab">Teater</span><span class="tab">Udstilling</span><span class="tab">Aeldre</span><span class="tab">Born</span><span class="tab">Motion</span><span class="tab">Diverse</span>
  </nav>

  <h2 class="list-title abs">Populaere Events</h2>
  <div class="sort abs">
    <span class="sort-label">Sorter efter</span>
    <span class="sort-box" style="width:46px">Populaere</span>
    <span class="sort-box" style="width:56px">Omrade <svg width="6" height="4" viewBox="0 0 6 4"><path d="M0 0h6L3 4z" fill="#777"/></svg></span>
    <span class="sort-box" style="width:30px;margin-left:2px">Dato</span>
    <span class="sort-box" style="width:31px">Pris</span>
  </div>

  <section class="events abs">
    <article class="event"><div class="event-img" role="img" aria-label="Young woman on a bicycle in autumn" style="background:linear-gradient(135deg,#8a5a2a,#d49a4a 55%,#6a7a4a)"></div><h3 class="event-title">Anders Vestby Koncert</h3><p class="event-desc">Lorem ipsum dolor sit amet, con-<br>sectetur adipisicing elit.</p><div class="event-links"><span class="see">Se event</span><span>Mine favoritter</span></div></article>
    <article class="event"><div class="event-img" role="img" aria-label="Young man with cap holding a skateboard" style="background:linear-gradient(135deg,#3b78b8,#8fb8dc 50%,#e8c650)"></div><h3 class="event-title">Anders Vestby Koncert</h3><p class="event-desc">Lorem ipsum dolor sit amet, con-<br>sectetur adipisicing elit.</p><div class="event-links"><span class="see">Se event</span><span>Mine favoritter</span></div></article>
    <article class="event"><div class="event-img" role="img" aria-label="Dancer leaping over a splash of blue paint" style="background:linear-gradient(135deg,#e8eaec,#c8d2da 55%,#4a6ec0)"></div><h3 class="event-title">Anders Vestby Koncert</h3><p class="event-desc">Lorem ipsum dolor sit amet, con-<br>sectetur adipisicing elit.</p><div class="event-links"><span class="see">Se event</span><span>Mine favoritter</span></div></article>

    <article class="event"><div class="event-img" role="img" aria-label="Photographer with camera over a city skyline" style="background:linear-gradient(135deg,#6f9cc8,#a9c0d4 50%,#4b4b4b)"></div><h3 class="event-title">Anders Vestby Koncert</h3><p class="event-desc">Lorem ipsum dolor sit amet, con-<br>sectetur adipisicing elit.</p><div class="event-links"><span class="see">Se event</span><span>Mine favoritter</span></div></article>
    <article class="event"><div class="event-img" role="img" aria-label="Cyclist riding past city towers" style="background:linear-gradient(180deg,#9cc0de,#b8c8d0 55%,#6b6f62)"></div><h3 class="event-title">Anders Vestby Koncert</h3><p class="event-desc">Lorem ipsum dolor sit amet, con-<br>sectetur adipisicing elit.</p><div class="event-links"><span class="see">Se event</span><span>Mine favoritter</span></div></article>
    <article class="event"><div class="event-img" role="img" aria-label="Group of friends looking at a tablet" style="background:linear-gradient(135deg,#8aaed0,#d8d8d8 50%,#4d6a8a)"></div><h3 class="event-title">Anders Vestby Koncert</h3><p class="event-desc">Lorem ipsum dolor sit amet, con-<br>sectetur adipisicing elit.</p><div class="event-links"><span class="see">Se event</span><span>Mine favoritter</span></div></article>

    <article class="event"><div class="event-img" role="img" aria-label="Theatre auditorium with red seats" style="background:linear-gradient(180deg,#1c140e,#8a3a1a 50%,#d25a2a)"></div><h3 class="event-title">Anders Vestby Koncert</h3><p class="event-desc">Lorem ipsum dolor sit amet, con-<br>sectetur adipisicing elit.</p><div class="event-links"><span class="see">Se event</span><span>Mine favoritter</span></div></article>
    <article class="event"><div class="event-img" role="img" aria-label="Visitors at an exhibition stand" style="background:linear-gradient(135deg,#c84a3a,#e0c0a0 50%,#7a8a9a)"></div><h3 class="event-title">Anders Vestby Koncert</h3><p class="event-desc">Lorem ipsum dolor sit amet, con-<br>sectetur adipisicing elit.</p><div class="event-links"><span class="see">Se event</span><span>Mine favoritter</span></div></article>
    <article class="event"><div class="event-img" role="img" aria-label="Family painting together at a table" style="background:linear-gradient(135deg,#f0ece6,#d8c0a8 55%,#6a4a3a)"></div><h3 class="event-title">Anders Vestby Koncert</h3><p class="event-desc">Lorem ipsum dolor sit amet, con-<br>sectetur adipisicing elit.</p><div class="event-links"><span class="see">Se event</span><span>Mine favoritter</span></div></article>

    <article class="event"><div class="event-img" role="img" aria-label="Elderly couple smiling" style="background:linear-gradient(135deg,#e8e4dc,#d8b8a0 55%,#b89a80)"></div><h3 class="event-title">Anders Vestby Koncert</h3><p class="event-desc">Lorem ipsum dolor sit amet, con-<br>sectetur adipisicing elit.</p><div class="event-links"><span class="see">Se event</span><span>Mine favoritter</span></div></article>
    <article class="event"><div class="event-img" role="img" aria-label="Baby in white blanket" style="background:linear-gradient(135deg,#f4f2f0,#ead8c8 60%,#d8b8a0)"></div><h3 class="event-title">Anders Vestby Koncert</h3><p class="event-desc">Lorem ipsum dolor sit amet, con-<br>sectetur adipisicing elit.</p><div class="event-links"><span class="see">Se event</span><span>Mine favoritter</span></div></article>
    <article class="event"><div class="event-img" role="img" aria-label="Two runners on a country road" style="background:linear-gradient(180deg,#7a9a4a,#8ba862 45%,#8a5a5a)"></div><h3 class="event-title">Anders Vestby Koncert</h3><p class="event-desc">Lorem ipsum dolor sit amet, con-<br>sectetur adipisicing elit.</p><div class="event-links"><span class="see">Se event</span><span>Mine favoritter</span></div></article>
  </section>

  <nav class="pager abs">
    <span class="prev"><svg width="5" height="8" viewBox="0 0 5 8"><path d="M4 0.5L1 4 4 7.5" fill="none" stroke="#444" stroke-width="1.4"/></svg>PREV</span>
    <span class="sep" style="margin-left:14px"></span>
    <span class="nums"><span>1</span><span>...</span><span>14</span><span>15</span><span>16</span><span>...</span><span>98</span></span>
    <span class="sep"></span>
    <span class="next" style="margin-left:12px">NEXT<svg width="5" height="8" viewBox="0 0 5 8"><path d="M1 0.5L4 4 1 7.5" fill="none" stroke="#444" stroke-width="1.4"/></svg></span>
  </nav>

  <div class="fav-head abs">Mine Favoriter
    <div class="fav-nav">
      <span><svg width="5" height="7" viewBox="0 0 5 7"><path d="M4 0.5L1 3.5 4 6.5" fill="none" stroke="#fff" stroke-width="1.2"/></svg></span>
      <span><svg width="5" height="7" viewBox="0 0 5 7"><path d="M1 0.5L4 3.5 1 6.5" fill="none" stroke="#fff" stroke-width="1.2"/></svg></span>
    </div>
  </div>
  <section class="fav-list abs">
    <div class="fav-item"><div class="fav-thumb" role="img" aria-label="Dancer over blue paint splash" style="background:linear-gradient(135deg,#e8eaec,#5a80c8)"></div><div><h4 class="fav-title">Lorem ipsum dolor sit</h4><p class="fav-text">Lorem ipsum dolor sit amet, consectetur adipisic-ing elit, sed do eiusmod tempor incididunt</p></div></div>
    <div class="fav-item" style="height:90px"><div class="fav-thumb" role="img" aria-label="Woman jogging in a field" style="background:linear-gradient(180deg,#9cc4e0,#7aa05a)"></div><div><h4 class="fav-title">Lorem ipsum dolor sit</h4><p class="fav-text">Lorem ipsum dolor sit amet, consectetur adipisic-ing elit, sed do eiusmod tempor incididunt</p></div></div>
    <div class="fav-item"><div class="fav-thumb" role="img" aria-label="Couple lying on a bed" style="background:linear-gradient(135deg,#f0f0f0,#c8b0a0)"></div><div><h4 class="fav-title">Lorem ipsum dolor sit</h4><p class="fav-text">Lorem ipsum dolor sit amet, consectetur adipisic-ing elit, sed do eiusmod tempor incididunt</p></div></div>
    <div class="fav-item" style="border:0"><div class="fav-thumb" role="img" aria-label="Woman with a rainbow umbrella" style="background:linear-gradient(135deg,#e04a4a,#f0c040 35%,#4aa06a 60%,#d0d0d0)"></div><div><h4 class="fav-title">Lorem ipsum dolor sit</h4><p class="fav-text">Lorem ipsum dolor sit amet, consectetur adipisic-ing elit, sed do eiusmod tempor incididunt</p></div></div>
  </section>
  <div class="fav-btn abs">Se mine favoritter</div>

  <div class="news-head abs">NewsLetter</div>
  <section class="news-body abs">
    <p class="news-text">Tilmeld dig KULTRAs myhedsbrev Bliv informeret omkring nye begivenheder og myheder fra KULTRA.Tilmeld dig ved at indtaste din emailadresse her</p>
    <div class="news-form">
      <div class="news-input">Enter Your Email</div>
      <div class="news-btn"><svg width="8" height="8" viewBox="0 0 12 12"><circle cx="5" cy="5" r="3.8" fill="none" stroke="#999" stroke-width="1.4"/><line x1="7.8" y1="7.8" x2="11" y2="11" stroke="#999" stroke-width="1.6"/></svg></div>
    </div>
  </section>

  <div class="promo-img abs" role="img" aria-label="Young man standing on a city street at night"></div>
  <div class="promo-corner abs"></div>
  <svg class="promo-plus abs" width="10" height="10" viewBox="0 0 10 10"><path d="M5 0v10M0 5h10" stroke="#fff" stroke-width="1.2"/></svg>
  <section class="promo-body abs">
    <h3 class="promo-title">Lorem ipsum dolor sit amet</h3>
    <p class="promo-text">Quisque accumsan eleifend dolor, nec bibendum nibh ultricies at. Nunc con-vallis risus sit amet augue</p>
  </section>

  <footer class="site-footer abs">
    <div class="copy">©2014 KULTRA . All Rights Reserved.</div>
    <nav class="foot-links">
      <span>Home</span><span class="bar">|</span><span>Om Kultra</span><span class="bar">|</span><span>Vilkar &amp; betingelser</span><span class="bar">|</span><span>Kobspolitik</span><span class="bar">|</span><span>Nyhedsbrev</span><span class="bar">|</span><span>Kontakt</span><span class="bar">|</span><span>Login?Registrer</span><span class="bar">|</span><span>Hjaelp</span><span class="bar">|</span><span>For arrangorer</span>
    </nav>
    <div class="social"><span></span><span></span><span></span><span></span></div>
  </footer>

</div>
</body>
</html>
```